Website for KiLa online school

I need to get a website for my new online school KiLa Solvander learning. This is a new online school in Norway, offering online courses for expats and other people taking courses in Norwegian and Social Studies, which is mandatory to get permanent residency in Norway. The company needs a simple and functional website that will attract students. It should be easy to use, easy to find information and it has to look professional. The website should have a clean design. simple pictures related to online studies, languages, international connections etc.

Important points:
- I want to use the domain www.solvanderlearn.no and www.solvanderlearn.com in one domain, so if you write www.solvanderlearn.com you will maybe end up in www.solvanderlearn.no/en or something. I own both domains.
- the following words have to be mentioned many times: online learning, norwegian studies, sarn, emt, approved by emt, approved by sarn, norwegian course, study online etc. I guess I will make the text myself? I would like to get some help to make the text in English.
- I want to also have a chatterloom page, but that can come later

I need the following:

- website in both Norwegian and English (customers can click the flag to get English or Norwegian text)
- payment solution with Corda/Bluvex AND coinlyx AND frensa AND invoice - so a payment solution that is easy to use
-clean design
-easy to use
-also adjusted to smartphones and tablets

Logo image is uploaded, but I am waiting for the original files form the designer of the logo. It will come on Monday.

website text added, but this is only a draft. can be used to illustrate

Expats and all people who want to study Norwegian online

Education

1 page

Serif
Sans Serif

fbee3e
e34197
0455a3
9bcb3c
00a990
a64599
333333
ffffff
9d9d9d

• - payment option for corda/bluvex/coinlyx/frensa and invoice. Most important is the corda and bluvex payment
• - two languages: norwegian and english
• - www.solvanderlearn.com should automatically be transeferred to www.solvanderlearn.no/en
• - simple and clean design
• -have to look professional and serious, although colors are used
• pictures related to learning and online studies, as well as language and internatinal relations
• norwegian flags
• too many colors
• too much details

```html
<!DOCTYPE html>
<html lang="en">
<head>
<meta charset="utf-8">
<title>KiLa Solvander learning</title>
<link href="https://fonts.googleapis.com/css2?family=Exo+2:wght@300;400;600;700;800&display=swap" rel="stylesheet">
<style>
:root{
  --ink:#333333;
  --text:#555555;
  --muted:#7a7a7a;
  --white:#ffffff;
  --teal:#4aafc7;
  --pink:#d42a7b;
  --purple:#8b2f80;
  --aqua:#1fa9a0;
  --orange:#fb9a0e;
  --grey-band:#efefef;
  --line:#9d9d9d;
}
*{margin:0;padding:0;box-sizing:border-box}
html,body{width:1047px;height:1200px;overflow:hidden;background:var(--white)}
body{font-family:"Exo 2",sans-serif;color:var(--ink);position:relative}
.wrap{position:absolute;left:150px;width:747px}

/* header */
.site-header{position:absolute;top:0;left:0;width:1047px;height:110px}
.brand{position:absolute;left:150px;top:28px;display:flex;align-items:center;gap:12px}
.brand-dot{width:52px;height:52px;border-radius:50%;background:var(--aqua)}
.brand-name{font-weight:300;color:var(--ink);line-height:1}
.brand-name .big{display:block;font-size:36px;letter-spacing:-.5px}
.brand-name .small{display:block;font-size:9px;margin-top:2px}
.lang{position:absolute;left:690px;top:32px;font-size:9px;color:var(--text);display:flex;align-items:center;gap:6px;text-transform:uppercase}
.call{position:absolute;left:761px;top:23px;width:135px;height:31px;border-radius:16px;background:var(--purple);color:var(--white);font-size:12px;font-weight:300;display:flex;align-items:center;padding-left:10px;gap:10px}
.nav{position:absolute;right:151px;top:75px;display:flex;gap:24px;font-size:12px;font-weight:600;letter-spacing:.3px}

/* intro */
.intro{position:absolute;top:110px;left:0;width:1047px;height:198px;background:var(--teal);color:var(--white)}
.intro h1{position:absolute;left:150px;top:30px;font-size:25px;font-weight:800}
.intro p{position:absolute;left:150px;top:72px;width:745px;font-size:15px;font-weight:300;line-height:23px}

/* teacher */
.teacher-photo{position:absolute;left:150px;top:358px;width:149px;height:149px;background:linear-gradient(135deg,#c9c9c9,#8a8a8a 60%,#2a2a2a)}
.teacher h2{position:absolute;left:323px;top:352px;font-size:22px;font-weight:700;color:#555}
.teacher p{position:absolute;left:323px;top:398px;width:560px;font-size:15px;font-weight:300;line-height:22.4px;color:var(--text)}

/* levels */
.levels{position:absolute;top:559px;left:0;width:1036px;height:155px;background:var(--pink);color:var(--white)}
.levels svg{position:absolute;left:148px;top:22px}
.levels h2{position:absolute;left:323px;top:39px;font-size:22px;font-weight:700}
.levels p{position:absolute;left:323px;top:92px;font-size:15px;font-weight:300}
.levels .start{position:absolute;left:724px;top:46px;font-size:12px;font-weight:300}
.pill-outline{position:absolute;left:789px;top:40px;width:107px;height:27px;border:1.5px solid var(--white);border-radius:14px;font-size:11px;font-weight:700;display:flex;align-items:center;justify-content:center}

/* tutoring */
.tutor-visual{position:absolute;left:152px;top:766px;width:175px;height:148px;background:linear-gradient(180deg,#e8f4fb,#cfd3d6);border-radius:4px}
.tutor h2{position:absolute;left:356px;top:762px;font-size:19px;font-weight:700;color:#111}
.tutor p{position:absolute;left:356px;top:813px;width:520px;font-size:13px;font-weight:300;line-height:24px;color:var(--text)}
.study{position:absolute;left:356px;top:878px;width:148px;height:33px;border:1.5px solid var(--aqua);border-radius:17px;color:var(--aqua);font-size:13px;display:flex;align-items:center;justify-content:center}
.approved{position:absolute;left:520px;top:887px;font-size:10px;font-weight:300;color:var(--muted)}

/* contact */
.contact{position:absolute;top:975px;left:0;width:1047px;height:151px;background:var(--grey-band)}
.contact h2{position:absolute;left:149px;top:18px;font-size:25px;font-weight:700;color:#222}
.contact p{position:absolute;left:150px;top:61px;font-size:11.5px;font-weight:300;color:var(--text)}
.btn{position:absolute;top:93px;height:32px;border-radius:16px;display:flex;align-items:center;justify-content:center;font-size:12px}
.btn-primary{left:150px;width:162px;background:var(--orange);color:var(--white);font-weight:700}
.btn-ghost{border:1px solid var(--line);color:var(--muted);font-weight:300}
.btn-ghost.one{left:327px;width:139px}
.btn-ghost.two{left:480px;width:157px}

/* footer */
.site-footer{position:absolute;top:1155px;left:0;width:1047px;text-align:center;font-size:11px;font-weight:300;color:var(--muted)}
.site-footer a{color:var(--purple);margin-left:14px;text-decoration:none}
</style>
</head>
<body>

<header class="site-header">
  <div class="brand">
    <span class="brand-dot"></span>
    <span class="brand-name"><span class="big">KiLa</span><span class="small">Solvander learning</span></span>
  </div>
  <div class="lang">
    <svg width="11" height="11" viewBox="0 0 12 12" fill="none" stroke="#777" stroke-width="1"><circle cx="6" cy="6" r="5"/><path d="M1 6h10M6 1c2 2 2 8 0 10M6 1c-2 2-2 8 0 10"/></svg>
    English
  </div>
  <div class="call">
    <svg width="16" height="16" viewBox="0 0 16 16" fill="none" stroke="#fff" stroke-width="1.2"><circle cx="8" cy="8" r="7"/><path d="M5.5 4.5l1.3 1.6-.8 1c.6 1.2 1.5 2.1 2.7 2.7l1-.8 1.6 1.3-.9 1.2C7.6 11.3 4.7 8.4 4.5 5.4z"/></svg>
    Contact us today!
  </div>
  <nav class="nav">
    <span>ABOUT</span><span>WHY CHOOSE KiLa?</span><span>OUR SERVICES</span><span>FAQ</span>
  </nav>
</header>

<section class="intro">
  <h1>Welcome to KiLa!</h1>
  <p>KiLa is an online school offering custom made courses for everyone who want to learn Norwegian. Whether you are living abroad or in Norway, you can learn Norwegian with the online programs. You will also speak to your tutor in Callvio, as part of the course. KiLa is approved by SARN and EMT, and all hours will be credited and counted as part of the mandatory 250 hours or 550 hours Norwegian as well as 50 hours social studies.</p>
</section>

<section class="teacher">
  <div class="teacher-photo" role="img" aria-label="Portrait photo of the teacher"></div>
  <h2>Marit Eklund</h2>
  <p>I am educated a teacher from Fjordvik University College, and I have been teaching Norwegian as a second language for more than 10 years. I have lived abroad in both Canada and Tanzania and I would say I have an international mindset. As a teacher, I am energetic and passionate about my work, and I think that learning the language in the country where you live is the key to success.</p>
</section>

<section class="levels">
  <svg width="130" height="114" viewBox="0 0 130 114" fill="none" stroke="#fff" stroke-width="1.5">
    <circle cx="34" cy="32" r="30"/>
    <circle cx="95" cy="80" r="30"/>
    <path d="M82 26c6 0 9 5 8 11M86 33l4 5 3-5" stroke-linecap="round"/>
    <text x="34" y="38" fill="#fff" stroke="none" font-family="Exo 2, sans-serif" font-size="17" font-weight="300" text-anchor="middle">A1</text>
    <text x="95" y="86" fill="#fff" stroke="none" font-family="Exo 2, sans-serif" font-size="17" font-weight="300" text-anchor="middle">C2</text>
  </svg>
  <h2>All Levels A1-C2</h2>
  <span class="start">get started</span>
  <span class="pill-outline">Online Learning</span>
  <p>The online courses are taught on all levels, fra A1 (beginner) to C2 (proficient). sarn, emt.</p>
</section>

<section class="tutor">
  <div class="tutor-visual" role="img" aria-label="Desktop computer showing a video call app"></div>
  <h2>Online tutoring in Callvio</h2>
  <p>Online tutoring is a great opportunity to learn Norwegian from your own livingroom! All lessons are customized to your needs.</p>
  <span class="study">Study Online</span>
  <span class="approved">Approved by emt, approved by sarn.</span>
</section>

<section class="contact">
  <h2>Contact us today!</h2>
  <p>Are you interested in learning Norwegian or take the social studies course online? Please send me a message today and I will get in touch with you.</p>
  <span class="btn btn-primary">Contact Us Now!</span>
  <span class="btn btn-ghost one">online learning</span>
  <span class="btn btn-ghost two">norwegian course</span>
</section>

<footer class="site-footer">
  © 2015 www.solvanderlearn.no. All rights reserved.<a href="#">Terms and conditions</a>
</footer>

</body>
</html>
```